Business Card Design Project

We need a redesign of our business card.
We are a Consulting Property Developer called The Kestrel Group
Updates

Thank you all for submissions. Just waiting on managment to decide.

Thank you,

Dorinda

Industry/Entity Type

Business

Requirements
Must have
• we like having the KG a focus in the back ground or on the side
Kestrel is our company colour

the wording - property development
and - premium accommodation

our website www.kestrelgroup-example.com.au

persons name
title

p: 1300 482917 f: 1300 482915 m: 0417593824
PO Box 5817, Brindlevale Qld 4178
e: admin@kestrelgroup-example.com.au

```html
<!DOCTYPE html>
<html lang="en">
<head>
<meta charset="utf-8">
<title>The Kestrel Group – Business Card</title>
<link rel="stylesheet" href="https://fonts.googleapis.com/css2?family=Arimo:ital@0;1&family=Open+Sans:wght@400&display=swap">
<style>
  :root {
    --kestrel: #98002e;
    --kestrel-soft: rgba(255,255,255,0.08);
    --silver: #a7a9ac;
    --paper: #ffffff;
    --ink-light: #ffffff;
  }
  * { margin: 0; padding: 0; box-sizing: border-box; }
  html, body { width: 1200px; height: 900px; overflow: hidden; background: var(--paper); }
  .canvas { position: relative; width: 1200px; height: 900px; }

  .card {
    position: absolute; top: 265px; width: 513px; height: 293px;
    box-shadow: 3px 4px 6px rgba(0,0,0,0.35);
    overflow: hidden;
  }
  .card--front { left: 73px; background: var(--paper); }
  .card--back { left: 630px; background: var(--kestrel); }

  .front__topband { position: absolute; left: 0; top: 0; width: 100%; height: 17px; background: var(--kestrel); }
  .front__topglow {
    position: absolute; left: 140px; right: 0; top: 20px; height: 3px;
    background: linear-gradient(90deg, rgba(152,0,46,0), rgba(152,0,46,0.8) 60%, rgba(152,0,46,0.15));
  }
  .front__divider-glow {
    position: absolute; left: 25px; width: 260px; top: 183px; height: 3px;
    background: linear-gradient(90deg, rgba(152,0,46,0), rgba(152,0,46,0.8) 55%, rgba(152,0,46,0));
  }
  .front__lowerband { position: absolute; left: 0; right: 0; top: 187px; bottom: 0; background: var(--kestrel); }

  .brand { position: absolute; display: flex; align-items: center; gap: 14px; }
  .brand__mark { width: 26px; height: 26px; border-radius: 50%; flex: none; }
  .brand__name { font-family: "Open Sans", sans-serif; font-weight: 400; font-size: 40px; letter-spacing: -0.5px; white-space: nowrap; }
  .brand__rule { position: absolute; height: 1px; }

  .card--front .brand { left: 40px; top: 66px; }
  .card--front .brand__mark { background: var(--kestrel); }
  .card--front .brand__name { color: var(--silver); }
  .card--front .brand__rule { left: 24px; width: 434px; top: 117px; background: var(--silver); }

  .contact-person { position: absolute; right: 10px; top: 150px; text-align: right; color: var(--kestrel); font-family: "Arimo", sans-serif; font-style: italic; }
  .contact-person__name { font-size: 17px; line-height: 20px; }
  .contact-person__title { font-size: 13px; line-height: 15px; }

  .services { position: absolute; left: 16px; top: 203px; list-style: none; color: var(--ink-light); font-family: "Arimo", sans-serif; font-style: italic; font-size: 14px; line-height: 17px; }
  .services li::before { content: "\25CF"; font-style: normal; font-size: 9px; margin-right: 6px; vertical-align: 2px; }

  .details { position: absolute; right: 10px; top: 203px; text-align: right; color: var(--ink-light); font-family: "Arimo", sans-serif; font-style: italic; font-size: 14px; line-height: 18px; font-style: italic; }

  .back__accent { position: absolute; left: 200px; top: -20px; width: 260px; height: 260px; border-radius: 50%; background: var(--kestrel-soft); }
  .card--back .brand { left: 28px; top: 108px; }
  .card--back .brand__mark { background: var(--ink-light); }
  .card--back .brand__name { color: var(--ink-light); }
  .card--back .brand__rule { left: 24px; width: 436px; top: 150px; background: rgba(255,255,255,0.7); }

  .website { position: absolute; left: 0; right: 0; top: 227px; text-align: center; color: var(--ink-light); font-family: "Arimo", sans-serif; font-style: italic; font-size: 17px; }
  .website__glow { position: absolute; left: 170px; width: 180px; top: 251px; height: 3px;
    background: linear-gradient(90deg, rgba(255,255,255,0), rgba(255,255,255,0.9) 50%, rgba(255,255,255,0)); }
</style>
</head>
<body>
<main class="canvas">
  <section class="card card--front" aria-label="Business card front">
    <div class="front__topband"></div>
    <div class="front__topglow"></div>
    <div class="brand">
      <span class="brand__mark"></span>
      <span class="brand__name">The Kestrel Group</span>
    </div>
    <div class="brand__rule" style="position:absolute;left:24px;width:434px;top:117px;height:1px;background:var(--silver);"></div>
    <div class="contact-person">
      <p class="contact-person__name">persons nameXXX</p>
      <p class="contact-person__title">titleXXX</p>
    </div>
    <div class="front__divider-glow"></div>
    <div class="front__lowerband">
      <ul class="services" style="top:16px;">
        <li>property development</li>
        <li>premium accommodation</li>
      </ul>
      <div class="details" style="top:16px;">
        <p>PO Box 5817, Brindlevale Qld 4178</p>
        <p>p: 1300 482917 m: 0417593824</p>
        <p>f: 1300 482915</p>
        <p>e: admin@kestrelgroup-example.com.au</p>
      </div>
    </div>
  </section>

  <section class="card card--back" aria-label="Business card back">
    <div class="back__accent"></div>
    <div class="brand">
      <span class="brand__mark"></span>
      <span class="brand__name">The Kestrel Group</span>
    </div>
    <div class="brand__rule"></div>
    <p class="website">www.kestrelgroup-example.com.au</p>
    <div class="website__glow"></div>
  </section>
</main>
</body>
</html>
```